Business Card Design

About Us
VaultNetix is a young and innovative company focusing on security and hosting solutions for global enterprise. To supply the high-performance, highly interconnected and low latency DDoS protection service, we distributed a large number of huge scrubbing centers all over the world. So VaultNetix is the first choice for enterprise to protect their network security.

Task detail
1. We hope that the business card can be filled with creativity, simple and technologe, the business card background is white, the business card text color and other colors are black, blue, green or your needs.

2. We need the source files provided by the successful bidder, such as *.psd, *.ai, etc.

3. One side contains the following:
-Logo
-Brin Sales Manager
-VAULTNETIX TECHNOLOGY CO., LIMITED
-Add:
9/F., Harmon Tower,
218 Pellow Street, Tai Hang, Kowloon,
HK
-Tel: 86-755-4172 0583
-Phone: 86-189 6041 3725
-Email: brin@vault-netix.com
-Web: www.vault-netix.com

4. The other side contains the following:
-Logo

5. Please find the attachment contains the logo PSD source files.

```html
<!DOCTYPE html>
<html lang="en">
<head>
<meta charset="utf-8">
<title>VaultNetix Business Card</title>
<link href="https://fonts.googleapis.com/css2?family=Arimo:wght@400;700&display=swap" rel="stylesheet">
<style>
  :root {
    --blue: #3bb4d3;
    --green: #73c043;
    --dark: #3b3b3b;
    --grey: #6c6a68;
    --ink: #2f2f2f;
    --paper: #ffffff;
    --backdrop: #e9e7e3;
  }
  * { box-sizing: border-box; margin: 0; padding: 0; }
  html, body {
    width: 1200px; height: 1000px; overflow: hidden;
    background: var(--backdrop);
    font-family: "Arimo", Arial, sans-serif;
    color: var(--ink);
  }
  .canvas { position: relative; width: 1200px; height: 1000px; }
  .card {
    position: absolute; width: 700px; height: 400px;
    background: var(--paper);
    box-shadow: 0 6px 18px rgba(0,0,0,0.18);
    overflow: hidden;
  }
  .card--info { left: 60px; top: 60px; }
  .card--logo { left: 440px; top: 540px; }

  .wordmark { display: flex; align-items: center; gap: 10px; }
  .wordmark__square { background: var(--blue); }
  .wordmark__name { font-weight: 700; color: var(--dark); line-height: 1; }
  .tagline { text-transform: uppercase; color: var(--ink); white-space: nowrap; }

  /* info side */
  .card--info .wordmark { position: absolute; left: 30px; top: 28px; }
  .card--info .wordmark__square { width: 30px; height: 30px; }
  .card--info .wordmark__name { font-size: 34px; }
  .card--info .tagline {
    position: absolute; left: 30px; top: 68px;
    font-size: 8.5px; letter-spacing: 2.4px;
  }
  .company-name {
    position: absolute; right: 30px; top: 58px;
    font-size: 15px; letter-spacing: 0.5px; color: var(--ink);
  }
  .rule { position: absolute; display: flex; height: 7px; }
  .rule span { display: block; height: 100%; }
  .rule .seg-blue { background: var(--blue); }
  .rule .seg-dark { background: var(--dark); }
  .rule .seg-green { background: var(--green); }
  .card--info .rule { left: 30px; top: 82px; width: 640px; }
  .card--info .seg-blue { width: 215px; }
  .card--info .seg-dark { width: 175px; }
  .card--info .seg-green { width: 250px; }

  .person { position: absolute; left: 0; right: 0; top: 158px; text-align: center; }
  .person__name { font-size: 21px; font-weight: 700; color: #555; }
  .person__title { font-size: 19px; color: #555; margin-top: 6px; }

  .contact-band { position: absolute; left: 0; bottom: 0; width: 700px; height: 112px; display: flex; }
  .contact-band__contacts {
    width: 250px; background: var(--blue); color: #fff;
    padding: 12px 0 0 18px; font-size: 14px; line-height: 22px;
  }
  .contact-band__spacer { width: 170px; background: var(--grey); }
  .contact-band__address {
    width: 280px; background: var(--green); color: #fff;
    padding: 12px 20px 0 0; font-size: 14px; line-height: 22px; text-align: right;
  }
  .contact-line { display: flex; align-items: center; gap: 8px; white-space: nowrap; }
  .contact-line svg { width: 13px; height: 13px; flex: none; }
  .contact-line--indent { padding-left: 21px; }

  /* logo side */
  .card--logo .rule { left: 40px; width: 620px; height: 8px; }
  .card--logo .rule--top { top: 26px; }
  .card--logo .rule--bottom { bottom: 26px; }
  .card--logo .seg-blue { width: 290px; }
  .card--logo .seg-dark { width: 110px; }
  .card--logo .seg-green { width: 220px; }
  .brand-block {
    position: absolute; left: 0; right: 0; top: 105px;
    display: flex; flex-direction: column; align-items: center;
  }
  .card--logo .wordmark__square { width: 56px; height: 56px; }
  .card--logo .wordmark__name { font-size: 72px; }
  .card--logo .tagline { font-size: 15px; letter-spacing: 7px; margin-top: 14px; }
  .site-url { font-size: 24px; color: var(--green); margin-top: 26px; }
</style>
</head>
<body>
<main class="canvas">

  <section class="card card--info" aria-label="Business card, contact side">
    <div class="wordmark">
      <span class="wordmark__square"></span>
      <span class="wordmark__name">VaultNetix</span>
    </div>
    <p class="tagline">Guarding a trusted network</p>
    <p class="company-name">VAULTNETIX TECHNOLOGY CO., LIMITED</p>
    <div class="rule"><span class="seg-blue"></span><span class="seg-dark"></span><span class="seg-green"></span></div>

    <div class="person">
      <p class="person__name">Brin</p>
      <p class="person__title">Sales Manager</p>
    </div>

    <div class="contact-band">
      <div class="contact-band__contacts">
        <p class="contact-line">
          <svg viewBox="0 0 16 16" aria-hidden="true"><path fill="#fff" d="M3.6 1.2l2.2 2.6-1.3 1.8c.8 1.9 2.1 3.2 4 4l1.8-1.3 2.6 2.2-1.2 2.4C6.5 13 3 9.5 1.2 4.4z"/></svg>
          86-755-4172 0583
        </p>
        <p class="contact-line contact-line--indent">86-189 6041 3725</p>
        <p class="contact-line">
          <svg viewBox="0 0 16 16" aria-hidden="true"><rect x="1" y="3" width="14" height="10" fill="#fff"/><path d="M1.5 3.5L8 9l6.5-5.5" stroke="#3bb4d3" stroke-width="1.3" fill="none"/></svg>
          brin@vault-netix.com
        </p>
        <p class="contact-line">
          <svg viewBox="0 0 16 16" aria-hidden="true"><g fill="none" stroke="#fff" stroke-width="1.3"><circle cx="8" cy="8" r="6.3"/><ellipse cx="8" cy="8" rx="2.8" ry="6.3"/><path d="M1.7 8h12.6M2.7 4.8h10.6M2.7 11.2h10.6"/></g></svg>
          www.vault-netix.com
        </p>
      </div>
      <div class="contact-band__spacer"></div>
      <div class="contact-band__address">
        <p>9/F., Harmon Tower,</p>
        <p>218 Pellow Street, Tai Hang, Kowloon,</p>
        <p>HK</p>
      </div>
    </div>
  </section>

  <section class="card card--logo" aria-label="Business card, logo side">
    <div class="rule rule--top"><span class="seg-blue"></span><span class="seg-dark"></span><span class="seg-green"></span></div>
    <div class="brand-block">
      <div class="wordmark">
        <span class="wordmark__square"></span>
        <span class="wordmark__name">VaultNetix</span>
      </div>
      <p class="tagline">Guarding a trusted network</p>
      <p class="site-url">www.vault-netix.com</p>
    </div>
    <div class="rule rule--bottom"><span class="seg-blue"></span><span class="seg-dark"></span><span class="seg-green"></span></div>
  </section>

</main>
</body>
</html>
```